New Design for Accounting Firm

CLIENT NAME: Corvantis
CURRENT WEBSITE: www.corvantisgroup-example.com.au

CLIENTS THE CLIENT LIKES:
http://velmarook.example.se/
http://www.tralvexio.example.biz/index.php
http://www.brindlequo.example.co.uk/
http://www.nerovaskellintrust.example.org/

COLOUR THEMES:
Colour theme to reflect the logo, with a leaning to blue in Accounting & Audit sections and green in Super section.

LOOK AND FEEL:
The look and feel needs to reflect an accessible culture and contemporary sensibility while still communicating our experience and stability as a professional company.

ABOUT:
The concept of 'Corvantis' is integral to our identity. Definition: 'The connection of creative ideas from a group of diverse individuals, applied with the end aim of solving practical problems'. See ''About Us'' on our website for more.

OTHER DETAILS:
Our three divisions (and service areas within each division) must be easily navigated as they related to very different users of the site. Two client sign in sections (Accounting & Super) must be easily distinguished to avoid user confusion.

MENU STRUCTURE:
* About
- includes history, values, our people, community etc
* Accounting & Advisory
- About
- Services
- Tax & Accounting
- Business Advisory
- Family Wealth Management
- Client Sign In
- Calculators
* Audit & Assurance
- About
- Services
* Corvantis Super
- About
- Individuals
- Services
- Advisers
- Services
- Portal Sign In
- Calculators
* Careers
* Newsletters
* Contact

REQUIREMENTS:
- Layered PSD form home and content pages
- No coding required, we use our own CMS to insert XHTML files into.
Updates

Hi Guys,

The client has asked for a non-cliche'd images in the design. If you'd like to try again with some images that represent the business but aren't your standard boring accounting-looking people, then please do! Cliche is a killer in design - please pump some creativity in!

Cheers,
Ted.

Reason: GUYS - PLEASE LISTEN TO THESE COMMENTS - I'VE SAID THEM TWICE NOW AND PEOPLE ARE STILL POSTING PROJECTS WITH CLICHED AND OBVIOUS ACCOUTNING TYPE IMAGES. USE YOUR CREATIVITY AND POST A DESIGN THAT IS OUTSIDE THE BOX WITH REGARDS TO THE IMAGES YOU ARE USING.

Reason: I am waiting to hear back from the client on their decision.

```html
<!DOCTYPE html>
<html lang="en">
<head>
<meta charset="utf-8">
<title>Corvantis — Accountants, Auditors and Super Fund Specialists</title>
<link rel="stylesheet" href="https://fonts.googleapis.com/css2?family=Arimo:wght@400;700&family=Cabin:wght@400;500&family=Noto+Sans:ital,wght@0,400;1,400&family=Tinos:ital,wght@0,700;1,700&display=swap">
<style>
  :root {
    --blue: #1160e6;
    --blue-dark: #0a4fd0;
    --green: #62f534;
    --green-line: #6fe83a;
    --orange: #f28a0c;
    --orange-soft: #f0993a;
    --amber: #f5a51a;
    --brown: #3b2510;
    --grey-text: #6b7880;
    --slate: #5a6b7c;
    --link: #1160e6;
    --panel-light: #f4f6f6;
    --rule: #cfd8de;
    --white: #ffffff;
  }
  * { box-sizing: border-box; margin: 0; padding: 0; }
  html, body { width: 1200px; height: 1134px; overflow: hidden; background: var(--white); }
  body { position: relative; font-family: "Noto Sans", sans-serif; color: var(--grey-text); }

  .top-band { position: absolute; left: 0; top: 0; width: 1200px; height: 12px; background: var(--blue); }
  .top-band::after { content: ""; position: absolute; left: 0; top: 12px; width: 100%; height: 4px; background: var(--green-line); }

  .brand { position: absolute; left: 82px; top: 16px; width: 225px; height: 54px; background: var(--white);
    border-radius: 0 0 8px 8px; box-shadow: 0 2px 6px rgba(0,0,0,.18); display: flex; align-items: center; gap: 10px; padding-left: 16px; }
  .brand-mark { width: 24px; height: 24px; background: var(--blue); }
  .brand-name { font-family: "Cabin", sans-serif; font-size: 36px; font-weight: 400; color: var(--blue); line-height: 1; }

  .utility-links { position: absolute; left: 741px; top: 31px; font-family: "Cabin", sans-serif; font-size: 15px; color: var(--blue); }
  .utility-links a { color: var(--blue); text-decoration: none; }
  .utility-links span { margin: 0 5px; }

  .enquiry-button { position: absolute; left: 929px; top: 32px; width: 191px; height: 30px; background: var(--amber);
    border-radius: 5px; color: var(--white); font-family: "Arimo", sans-serif; font-weight: 700; font-size: 17px;
    display: flex; align-items: center; justify-content: center; letter-spacing: .3px; }

  .main-nav { position: absolute; left: 84px; top: 89px; height: 31px; display: flex; background: var(--blue); }
  .main-nav a { height: 31px; display: flex; align-items: center; justify-content: center; color: var(--white);
    font-family: "Arimo", sans-serif; font-weight: 700; font-size: 14.5px; text-decoration: none; border-right: 1px solid rgba(255,255,255,.85); }
  .main-nav a:last-child { border-right: 0; }

  .division-panel { position: absolute; top: 137px; height: 299px; border-radius: 3px; }
  .panel-blue { left: 87px; width: 679px; background: var(--blue); }
  .panel-green { left: 780px; width: 338px; background: var(--green); }
  .panel-divider { position: absolute; left: 348px; top: 39px; width: 1px; height: 194px; background: rgba(255,255,255,.8); }

  .division-title { position: absolute; font-family: "Cabin", sans-serif; font-size: 27px; color: var(--white); text-align: center; line-height: 1.05; }
  .icon-frame { position: absolute; width: 154px; height: 124px; border: 2px solid var(--white); border-radius: 6px; }
  .icon-fill-blue { background: linear-gradient(160deg, #1a68ea, #0d55d6); }
  .icon-fill-green { background: linear-gradient(160deg, #6df73f, #e38a2a 140%); }

  .panel-button { position: absolute; width: 158px; height: 40px; display: flex; align-items: center; justify-content: center;
    font-family: "Arimo", sans-serif; font-weight: 700; font-size: 18px; color: var(--white); letter-spacing: .5px; }
  .btn-orange { background: var(--orange); }
  .btn-green { background: var(--green); }
  .btn-brown { background: var(--brown); }

  .welcome { position: absolute; left: 88px; top: 451px; width: 650px; }
  .welcome-title { font-family: "Tinos", serif; font-weight: 700; font-size: 29px; color: var(--blue); line-height: 36px;
    width: 575px; border-bottom: 1px solid var(--green-line); padding-bottom: 1px; }
  .welcome-body { margin-top: 20px; margin-left: 3px; font-size: 13.4px; line-height: 21.1px; color: var(--grey-text); width: 650px; }
  .welcome-body p { margin-bottom: 21.1px; }
  .welcome-body ul { list-style: none; margin-bottom: 21.1px; }
  .welcome-body li { color: var(--link); }
  .read-more { position: absolute; left: 630px; top: 1008px; font-family: "Tinos", serif; font-weight: 700; font-size: 14px; color: var(--blue); text-decoration: none; }

  .column-rule { position: absolute; left: 762px; top: 488px; width: 1px; height: 550px; background: var(--rule); }

  .newsletter { position: absolute; left: 784px; top: 480px; width: 330px; height: 147px; background: var(--orange-soft); border-radius: 22px; }
  .newsletter-title { position: absolute; left: 0; top: 8px; width: 100%; text-align: center; font-family: "Tinos", serif; font-style: italic; font-weight: 700; font-size: 28px; color: var(--slate); }
  .newsletter-input { position: absolute; left: 48px; top: 56px; width: 239px; height: 25px; background: var(--white); border: 1px solid #7a7a7a; }
  .newsletter-submit { position: absolute; left: 112px; top: 107px; width: 108px; height: 25px; background: #7f8c8d; color: var(--white);
    font-family: "Arimo", sans-serif; font-weight: 700; font-size: 17px; display: flex; align-items: center; justify-content: center; letter-spacing: .5px; }

  .testimonials { position: absolute; left: 790px; top: 655px; width: 317px; height: 375px; background: var(--panel-light); border-radius: 6px; overflow: hidden; }
  .testimonials-title { position: absolute; left: 17px; top: 10px; width: 278px; text-align: center; font-family: "Tinos", serif; font-weight: 700; font-size: 22px; color: var(--slate);
    border-bottom: 1px solid var(--slate); padding-bottom: 4px; }
  .testimonials-body { position: absolute; left: 23px; top: 64px; width: 280px; font-size: 13.4px; line-height: 21.1px; color: var(--grey-text); }
  .testimonials-body p { margin-bottom: 21.1px; }

  .footer-rule { position: absolute; left: 0; top: 1087px; width: 1200px; height: 2px; background: var(--blue); }
  .footer-links { position: absolute; left: 76px; top: 1097px; font-size: 10.4px; color: #97a3ab; letter-spacing: .1px; }
  .footer-links span { margin: 0 4px; }
  .copyright { position: absolute; right: 66px; top: 1097px; font-size: 10.4px; font-style: italic; color: var(--blue); }
</style>
</head>
<body>
  <div class="top-band"></div>

  <div class="brand">
    <span class="brand-mark"></span>
    <span class="brand-name">Corvantis</span>
  </div>

  <div class="utility-links"><a href="#">Careers</a><span>I</span><a href="#">Newsletters</a></div>
  <div class="enquiry-button">SEND AN ENQUIRY</div>

  <nav class="main-nav">
    <a href="#" style="width:87px">HOME</a>
    <a href="#" style="width:99px">WHO WE ARE</a>
    <a href="#" style="width:234px">ACCOUNTING &amp; ADVISORY</a>
    <a href="#" style="width:173px">AUDIT &amp; ASSURANCE</a>
    <a href="#" style="width:238px">SELF MANAGED SUPER FUNDS</a>
    <a href="#" style="width:80px">LINKS</a>
    <a href="#" style="width:124px">CONTACT US</a>
  </nav>

  <section class="division-panel panel-blue">
    <h2 class="division-title" style="left:20px;top:18px;width:300px;">Accounting &amp; Advisory</h2>
    <div class="icon-frame icon-fill-blue" style="left:98px;top:81px;" role="img" aria-label="Illustration of a tax question, numbered list and report sheet"></div>
    <div class="panel-button btn-orange" style="left:95px;top:230px;">CLIENT&nbsp; LOGIN</div>

    <div class="panel-divider"></div>

    <h2 class="division-title" style="left:358px;top:20px;width:290px;">Audit &amp; Assurance</h2>
    <div class="icon-frame icon-fill-blue" style="left:426px;top:84px;" role="img" aria-label="Illustration of papers, a dollar sign and a 100% tick">
      <svg width="150" height="120" viewBox="0 0 150 120" aria-hidden="true">
        <rect x="76" y="62" width="34" height="32" fill="none" stroke="#fff" stroke-width="2"/>
        <path d="M80 74 L92 88 L124 56" fill="none" stroke="#fff" stroke-width="7" stroke-linecap="round" stroke-linejoin="round"/>
      </svg>
    </div>
    <div class="panel-button btn-green" style="left:423px;top:227px;">KNOW MORE</div>
  </section>

  <section class="division-panel panel-green">
    <h2 class="division-title" style="left:14px;top:10px;width:310px;">Self Managed Super<br>Funds</h2>
    <div class="icon-frame icon-fill-green" style="left:92px;top:82px;" role="img" aria-label="Illustration of a money bag with stacked gold coins"></div>
    <div class="panel-button btn-brown" style="left:88px;top:226px;">CLIENT&nbsp; LOGIN</div>
  </section>

  <main class="welcome">
    <h1 class="welcome-title">Welcome to Corvantis</h1>
    <div class="welcome-body">
      <p>Corvantis is a Tasmanian based firm which offers the skills of Accountants, Business Performace Advisers, Auditors and Self Managed Super Fund Specialists.</p>
      <p>From our offices in Devonport and Hobart we deliver services across three divisions:</p>
      <ul>
        <li>&gt; AG Corvantis Chartered Accountants</li>
        <li>&gt; Corvantis Audit @ Assurance</li>
        <li>&gt; Corvantis Super</li>
      </ul>
      <p>Through our three divisions, our clients benefit from the application of specialist skills and systems, developed in relevant areas of expertise.&nbsp; At the same time, our teams are skilled at integrating their knowledge with the common goal of meeting our clients comprehensive needs.</p>
      <p>Across the firm we deliver services in a wide range of industries, to individuals, businesses, corporations and financial advisers.</p>
      <p>Our services include:</p>
      <ul>
        <li>&gt; Accounting and Taxation</li>
        <li>&gt; Corporate and Business Advice</li>
        <li>&gt; Family Wealth Management</li>
        <li>&gt; Audit and Assurance</li>
        <li>&gt; Self Managed Super Fund Administration</li>
      </ul>
    </div>
  </main>
  <a class="read-more" href="#">READ MORE....</a>

  <div class="column-rule"></div>

  <aside class="newsletter">
    <h3 class="newsletter-title">Join our Newsletter</h3>
    <div class="newsletter-input"></div>
    <div class="newsletter-submit">SUBMIT</div>
  </aside>

  <aside class="testimonials">
    <h3 class="testimonials-title">Here what our users say!</h3>
    <div class="testimonials-body">
      <p>“Corvantis is a Tasmanian based firm which offers the skills of Accountants, Business Performace Advisers, Auditors and Self Managed Super Fund Specialists. Self Advisers, Auditors and Self Managed Super Fund Specialists. Performace Advisers, Auditors and Self Managed Super Fund Specialists. Performace Advisers, Auditors and Self Managed Super Fund Specialists.”</p>
      <p>- Dale Ferrow, Canada</p>
      <p>“Corvantis is a Tasmanian based firm which offers the skills of Accountants.”</p>
    </div>
  </aside>

  <div class="footer-rule"></div>
  <footer>
    <div class="footer-links">HOME<span>I</span>WHO WE ARE<span>I</span>ACCOUNTING &amp; ADVISORY<span>I</span>AUDIT &amp; ASSURANCE<span>I</span>SELF MANAGED SUPER FUNDS<span>I</span>LINKS<span>I</span>CONTACT US<span>I</span>CAREERS<span>I</span>NEWSLETTERS<span>I</span>PRIVACY</div>
    <div class="copyright">Copyright@2011&nbsp; Corvantis Group</div>
  </footer>
</body>
</html>
```